Orbelle Communications Business Card Competition

High quality international communications for consumers and business. We are re-designing our website and re-branding. Our current (old) website can be viewed at www.reachorbelle.example Vision statement - We enable people and communities to build and maintain strong and lasting global connections This is the brand image that we are trying to get across: •Quality—Orbelle delivers the highest quality connections wherever you need to communicate. •Service—Orbelle is always there for you, with the industry-leading service that promises to ensure that every experience is a good one. •Value—Orbelle provides the best value in the global communications market. Typical messaging: Connecting the Most Important People in the World. Focus on international communications

We want to convey our service quality and that we really care about the service we provide and our customers. We want to emphasis the international aspect of our business. We want to make it personal, but it has to relate to business as well as individuals. We want the card to be unique in design but clear enough to read. We want a business prospect as well as a regular person to look at our card and know what we do.

Target Market(s)

Consumer - multi-ethnic consumer base living in the US calling, texting and connecting with family and friends in countries around the world 2. Busine

Industry/Entity Type

Communications

Requirements
Must have
• 1. Logo must be visible (see uploaded)

2.Artist can use variations of our company colors to accent our logo:

Hex Codes:
Magenta = ab3179
Blue = 2895c0
Green = 8ebb3f

3.Must have the following slogan visible: Because Every Word Matters

below are the required data fields:

Full Name: Mark Tilby
Position: Chief Financial Officer
Office: +1 614-382-9071 ext.208
Mobile: +1 614-382-9071
Fax: +1 614-382-9071
Email: MarkT@reachorbelle.example
URL: www.reachorbelle.example
Address:
31820 Harlow Lane
suite 412
Ashburn, VA 20153
USA

Nice to have
• Die cut cards or uniquely shaped cards would be interesting to see but not required

```html
<!DOCTYPE html>
<html lang="en">
<head>
<meta charset="utf-8">
<title>Orbelle Communications – Mark Tilby</title>
<link href="https://fonts.googleapis.com/css2?family=Mulish:wght@300;400&display=swap" rel="stylesheet">
<style>
  :root {
    --magenta: #a814c2;
    --green: #8cec0a;
    --blue: #41b6df;
    --teal: #4cbfc6;
    --ink: #111111;
    --grey-text: #9a9a9a;
    --bg-light: #ffffff;
    --bg-edge: #d9d9d9;
  }
  html, body {
    margin: 0;
    padding: 0;
    overflow: hidden;
    background: #ffffff;
  }
  .card {
    position: relative;
    width: 1200px;
    height: 693px;
    overflow: hidden;
    font-family: "Mulish", sans-serif;
    font-weight: 300;
    color: var(--ink);
    background: radial-gradient(ellipse 60% 65% at 68% 55%, var(--bg-light) 0%, #f4f4f4 55%, var(--bg-edge) 100%);
  }
  .card-shapes {
    position: absolute;
    inset: 0;
  }
  .contact-list {
    position: absolute;
    left: 40px;
    top: 146px;
    width: 530px;
    margin: 0;
    padding: 0;
    list-style: none;
    font-size: 32px;
    line-height: 36px;
    white-space: nowrap;
  }
  .contact-list .contact-email,
  .contact-list .contact-url {
    font-size: 30px;
    line-height: 38px;
  }
  .address {
    position: absolute;
    left: 92px;
    width: 400px;
    top: 384px;
    text-align: center;
    font-size: 31px;
    line-height: 37px;
  }
  .address-label {
    font-size: 46px;
    line-height: 56px;
    margin-bottom: 8px;
  }
  .brand {
    position: absolute;
    left: 632px;
    top: 118px;
    width: 520px;
  }
  .brand-row {
    display: flex;
    align-items: center;
    gap: 16px;
  }
  .brand-mark {
    flex: none;
    width: 40px;
    height: 40px;
    border-radius: 50%;
    background: var(--blue);
  }
  .brand-name {
    font-size: 40px;
    font-weight: 400;
    white-space: nowrap;
    color: var(--magenta);
  }
  .slogan {
    margin-top: 22px;
    font-size: 25px;
    letter-spacing: 5px;
    white-space: nowrap;
    color: var(--grey-text);
  }
  .name-tag {
    position: absolute;
    left: 582px;
    top: 401px;
    width: 282px;
    height: 85px;
    display: flex;
    align-items: center;
    padding-left: 20px;
    box-sizing: border-box;
    font-size: 44px;
    background: var(--green);
    box-shadow: 6px 10px 14px rgba(0,0,0,0.35);
  }
  .title-tag {
    position: absolute;
    left: 631px;
    top: 488px;
    width: 278px;
    height: 37px;
    display: flex;
    align-items: center;
    justify-content: center;
    font-size: 22px;
    background: var(--blue);
    box-shadow: 6px 8px 12px rgba(0,0,0,0.3);
  }
</style>
</head>
<body>
<div class="card">
  <svg class="card-shapes" width="1200" height="693" viewBox="0 0 1200 693" aria-hidden="true">
    <defs>
      <filter id="panel-shadow" x="-20%" y="-20%" width="140%" height="150%">
        <feDropShadow dx="8" dy="14" stdDeviation="16" flood-color="#000" flood-opacity="0.35"/>
      </filter>
    </defs>
    <path d="M0 0 H470 Q440 57 380 57 H0 Z" fill="var(--green)"/>
    <g stroke="var(--ink)" stroke-width="7">
      <line x1="1140" y1="-5" x2="1205" y2="60"/>
      <line x1="1160" y1="-5" x2="1205" y2="40"/>
      <line x1="1180" y1="-5" x2="1205" y2="20"/>
      <line x1="-5" y1="560" x2="130" y2="698"/>
      <line x1="-5" y1="585" x2="108" y2="698"/>
      <line x1="-5" y1="610" x2="85" y2="698"/>
      <line x1="-5" y1="635" x2="62" y2="698"/>
    </g>
    <g filter="url(#panel-shadow)" fill="var(--magenta)">
      <path d="M0 124 H572 Q582 124 582 134 V453 Q582 463 572 463 H0 Z"/>
      <circle cx="282" cy="418" r="214"/>
    </g>
    <g role="img" aria-label="Globe showing the Americas">
      <circle cx="1115" cy="540" r="152" fill="var(--teal)"/>
    </g>
    <path d="M722 693 Q735 632 800 632 H1200 V693 Z" fill="var(--magenta)"/>
  </svg>

  <div class="brand">
    <div class="brand-row">
      <span class="brand-mark"></span>
      <span class="brand-name">Orbelle Communications</span>
    </div>
    <div class="slogan">Because Every Word Matters</div>
  </div>

  <ul class="contact-list">
    <li>Office: +1 614-382-9071 ext.208</li>
    <li>Mobile: +1 614-382-9071</li>
    <li>Fax: +1 614-382-9071</li>
    <li class="contact-email">Email: MarkT@reachorbelle.example</li>
    <li class="contact-url">URL: www.reachorbelle.example</li>
  </ul>

  <div class="address">
    <div class="address-label">Address:</div>
    <div>31820 Harlow Lane</div>
    <div>suite 412</div>
    <div>Ashburn, VA 20153</div>
    <div>USA</div>
  </div>

  <div class="name-tag">Mark Tilby</div>
  <div class="title-tag">Chief Financial Officer</div>
</div>
</body>
</html>
```